Flyer Design sales and lettings

We need a double sided flyer for our Estate and Letting agency. We have just moved in to 16th century office and expanded our offer to commercial and residential sales (previously we were targeted on lettings only). We are based in small rural town in Midlands, UK.Any photos, graphics will need to be linked to our location (please dont use skyscrapers :)One side of our flyer will have to treat about lettings and our offer - 7% plus vat commission on all new lettings, no extra costs, rent guarantee insurance, we are open 6 days a week and available 24/7.Please insert information about our commercial department on this side as well. "Landlords! Did you know that we also do commercial lettings? Call us on 01427918305 for best offer in the area. Other side informing clients about our sales offer 0.7% plus vat on all new sales instructions, free market appraisal, no up front costs, no sale no fee, we are open 6 days a week and available 24/7Here is our website: www.morvenhomesteads.uk We are members of KTV, BLW and leasewell9 (logos attached)Thank you Tomasz Wielgorek
Updates

Target Market(s)

Landlords and vendors in local area

Industry/Entity Type

Real Estate Agent

Font styles to use
Decorative
Script

Requirements
Must have
• all points stated in descriptip
Nice to have
• our logo or parts of it incorporated in design, elegant retro, stylish effcts.
• Silver/Charcoal coulour with retro gold theme.
Should not have
• modern, city accents.

```html
<!DOCTYPE html>
<html lang="en">
<head>
<meta charset="utf-8">
<title>Morven Homesteads – Lettings Flyer</title>
<link rel="stylesheet" href="https://fonts.googleapis.com/css2?family=Oswald:wght@500;600&family=EB+Garamond:wght@500;700&family=Open+Sans:ital,wght@0,400;0,600;1,600&family=Arimo:wght@700&display=swap">
<style>
  :root{
    --gold:#a9843a;
    --gold-light:#d9bb72;
    --gold-dark:#6f531c;
    --charcoal:#1c1c1c;
    --black:#111;
    --silver:#b9b9b9;
    --white:#fff;
    --page:#e6e2da;
  }
  *{margin:0;padding:0;box-sizing:border-box}
  html,body{width:907px;height:1200px;overflow:hidden;background:var(--page)}
  .flyer{position:absolute;left:101px;top:94px;width:705px;height:1012px;background:var(--white);overflow:hidden;box-shadow:0 2px 10px rgba(0,0,0,.15)}
  .flyer-shapes{position:absolute;inset:0}
  .brand-name{position:absolute;left:57px;top:50px;font:500 25px/1.2 "EB Garamond",serif;color:var(--gold-dark)}
  .brand-areas{position:absolute;left:18px;top:112px;width:300px;display:flex;justify-content:space-between;font:500 11px/1.2 "EB Garamond",serif;color:#777}
  .headline{position:absolute;left:20px;top:398px}
  .headline-main{font:600 70px/.92 "Oswald",sans-serif;letter-spacing:1px;background:linear-gradient(180deg,var(--gold-light),var(--gold) 55%,var(--gold-dark));-webkit-background-clip:text;background-clip:text;color:transparent}
  .headline-sub{font:500 39px/1 "Oswald",sans-serif;color:var(--black);letter-spacing:.5px;margin-top:4px}
  .headline-tag{font:700 17px/1.2 "EB Garamond",serif;color:var(--black);letter-spacing:.3px;margin-top:1px}
  .burst-text{position:absolute;left:458px;top:302px;width:196px;text-align:center;color:var(--white)}
  .burst-from{font:500 28px/1 "EB Garamond",serif}
  .burst-rate{font:700 41px/1.15 "Arimo",sans-serif}
  .burst-vat{font:700 38px/1 "Arimo",sans-serif}
  .ribbon-label{position:absolute;left:229px;top:540px;width:240px;text-align:center;font:700 21px/32px "Arimo",sans-serif;color:var(--white)}
  .letting-points{position:absolute;list-style:none;color:var(--white);font:italic 600 12px/17px "Open Sans",sans-serif}
  .letting-points.col-left{left:22px;top:620px;width:300px}
  .letting-points.col-right{left:374px;top:627px;width:300px}
  .letting-points li{position:relative;padding-left:18px;margin-bottom:2px}
  .letting-points li::before{content:"";position:absolute;left:0;top:4px;width:9px;height:9px;border-radius:50%;background:var(--gold-light)}
  .contact{position:absolute;left:24px;top:804px;font:400 12.5px/16.4px "Open Sans",sans-serif;font-style:normal;color:var(--black)}
  .contact-label,.contact-title{font:700 13px/16.4px "EB Garamond",serif;color:var(--gold)}
  .contact-phone{font:600 12.5px "Open Sans",sans-serif;color:var(--black)}
  .members{position:absolute;left:22px;top:940px;display:flex;gap:22px;align-items:center;font:600 15px "Open Sans",sans-serif;color:var(--charcoal)}
  .member{display:flex;align-items:center;gap:5px}
  .member-mark{width:11px;height:11px;background:var(--gold)}
  .offers-title{position:absolute;right:32px;top:766px;font:700 25px/1.2 "EB Garamond",serif;color:var(--black)}
  .offers{position:absolute;right:30px;top:806px;list-style:none;text-align:right;color:var(--white);font:italic 600 12.5px/17px "Open Sans",sans-serif}
  .offers li{position:relative;padding-right:17px;margin-bottom:5px}
  .offers li::after{content:"";position:absolute;right:0;top:4px;width:8px;height:8px;border-radius:50%;background:var(--black)}
  .social{position:absolute;right:32px;top:948px;display:flex;gap:14px;font:600 11px "Open Sans",sans-serif;color:var(--black)}
  .social span{display:flex;align-items:center;gap:4px}
  .social span::before{content:"";width:8px;height:8px;border-radius:50%;background:var(--black)}
</style>
</head>
<body>
<main class="flyer">
  <svg class="flyer-shapes" viewBox="0 0 705 1012" width="705" height="1012">
    <defs>
      <linearGradient id="goldFill" x1="0" y1="0" x2="1" y2="1">
        <stop offset="0" stop-color="#d9bb72"/><stop offset=".5" stop-color="#a9843a"/><stop offset="1" stop-color="#6f531c"/>
      </linearGradient>
      <linearGradient id="photoTone" x1="0" y1="0" x2="0" y2="1">
        <stop offset="0" stop-color="#c8d3dc"/><stop offset=".35" stop-color="#9b5a48"/><stop offset="1" stop-color="#4f4a3f"/>
      </linearGradient>
      <linearGradient id="sketchTone" x1="0" y1="0" x2="1" y2="0">
        <stop offset="0" stop-color="#d6d6d6"/><stop offset=".5" stop-color="#b5b5b5"/><stop offset="1" stop-color="#dcdcdc"/>
      </linearGradient>
      <linearGradient id="bandFill" x1="0" y1="0" x2="0" y2="1">
        <stop offset="0" stop-color="#2a2a2a"/><stop offset="1" stop-color="#111"/>
      </linearGradient>
    </defs>

    <rect class="house-photo" x="360" y="0" width="345" height="300" fill="url(#photoTone)" role="img" aria-label="Photograph of a red-brick semi-detached house"/>
    <path class="gold-swoosh" d="M220 300 Q460 215 705 228 L705 605 L575 600 Q495 372 220 300 Z" fill="url(#goldFill)"/>
    <path d="M215 298 Q470 230 705 236" fill="none" stroke="#fff" stroke-width="6"/>
    <path d="M205 302 Q495 372 575 600" fill="none" stroke="#1c1c1c" stroke-width="9"/>
    <path d="M190 306 Q482 382 560 602" fill="none" stroke="#b9b9b9" stroke-width="3"/>

    <circle cx="185" cy="55" r="230" fill="#fff"/>
    <circle cx="185" cy="55" r="230" fill="none" stroke="url(#goldFill)" stroke-width="12"/>
    <circle cx="185" cy="55" r="244" fill="none" stroke="#1c1c1c" stroke-width="4" stroke-dasharray="260 2000" stroke-dashoffset="-170"/>

    <rect class="brand-sketch" x="18" y="131" width="300" height="56" rx="2" fill="url(#sketchTone)" role="img" aria-label="Line drawings of lettings, sales, residential and commercial buildings"/>
    <rect class="brand-keys" x="135" y="88" width="34" height="122" rx="10" fill="#b8924a" role="img" aria-label="Illustration of a pair of antique keys"/>

    <polygon class="price-burst" fill="#111" stroke="#fff" stroke-width="3"
      points="556,244 571.6,263.2 592.5,249.8 601.4,272.9 625.4,266.5 626.7,291.3 651.5,292.6 645.1,316.6 668.2,325.5 654.8,346.4 674,362 654.8,377.6 668.2,398.5 645.1,407.4 651.5,431.4 626.7,432.7 625.4,457.5 601.4,451.1 592.5,474.2 571.6,460.8 556,480 540.4,460.8 519.5,474.2 510.6,451.1 486.6,457.5 485.3,432.7 460.5,431.4 466.9,407.4 443.8,398.5 457.2,377.6 438,362 457.2,346.4 443.8,325.5 466.9,316.6 460.5,292.6 485.3,291.3 486.6,266.5 510.6,272.9 519.5,249.8 540.4,263.2"/>

    <path d="M0 578 Q330 508 705 598" fill="none" stroke="url(#goldFill)" stroke-width="5"/>
    <path class="dark-band" d="M0 590 Q330 520 705 610 L705 700 Q480 730 395 842 Q200 796 0 782 Z" fill="url(#bandFill)"/>
    <path d="M0 792 Q200 804 392 850" fill="none" stroke="url(#goldFill)" stroke-width="4"/>
    <path class="gold-corner" d="M385 1012 L385 856 Q470 748 705 712 L705 1012 Z" fill="url(#goldFill)"/>

    <path class="ribbon" d="M229 540 L469 540 L459 556 L469 572 L229 572 L239 556 Z" fill="url(#goldFill)"/>
  </svg>

  <div class="brand-name">Morven Homesteads</div>
  <div class="brand-areas"><span>Lettings</span><span>Sales</span><span>Residential</span><span>Commercial</span></div>

  <div class="burst-text">
    <div class="burst-from">Starting from</div>
    <div class="burst-rate">7% plus</div>
    <div class="burst-vat">VAT</div>
  </div>

  <section class="headline">
    <h1 class="headline-main">LANDLORDS!</h1>
    <p class="headline-sub">DID YOU KNOW THAT</p>
    <p class="headline-tag">WE ALSO DO COMMERCIAL LETTINGS?</p>
  </section>

  <div class="ribbon-label">About lettings</div>

  <ul class="letting-points col-left">
    <li>New shop ground floor suitable for all uses.<br>Size - 23.3 sq/m (250.9 sq/ft) plus cellar</li>
    <li>Ideal for a small business startup!!!<br>Don't miss the opportunity</li>
    <li>The shop is situated in Mill Lane, Ashcombe<br>It is close to the Town Centre</li>
    <li>The shop will suit any client starting up a new business adventure. Ideal business opportunity</li>
  </ul>
  <ul class="letting-points col-right">
    <li>The property is available by way of leasehold on flexible terms, subject to contract.<br>Terms to be agreed</li>
    <li>A1/A2 use. Any interested parties should make their own enquires for use by the local planning authority.</li>
  </ul>

  <address class="contact">
    <div class="contact-title">Contact us</div>
    Alder House<br>
    14 Market Row Ashcombe<br>
    AB12 3CD United Kingdom<br>
    <span class="contact-label">Office telephone number:</span> <span class="contact-phone">01427-918-305</span><br>
    <span class="contact-label">Email:</span> office@morvenhomesteads.uk<br>
    <span class="contact-label">Email:</span> office@ashcombelettings.co.uk<br>
    <span class="contact-label">Website:</span>www.morvenhomesteads.uk
  </address>

  <div class="members">
    <span class="member"><i class="member-mark"></i>BLW</span>
    <span class="member">Homefindr</span>
    <span class="member">KTV</span>
    <span class="member">leasewell9</span>
  </div>

  <h2 class="offers-title">Our offers</h2>
  <ul class="offers">
    <li>7% plus vat commission on<br>all new lettings</li>
    <li>No extra costs<br>Rent guarantee insurance</li>
    <li>We are open 6 days a week<br>and available 24/7</li>
  </ul>

  <div class="social"><span>Chatter</span><span>Facenet</span><span>Newsfeed</span><span>Vidstream</span></div>
</main>
</body>
</html>
```